Business card design needed

It's a new business in town.Something so the name stands out.I need a logo for the B.R.K
I may all so use the design as a sign on a building

Contact Information for Business Card

B.R.K
Brackenvale Auto Detailing
42 Tillbury Crs
Brackenvale Vic 3819
Ph:(03)58264027
Mob:0417392658

```html
<!DOCTYPE html>
<html lang="en">
<head>
<meta charset="utf-8">
<title>B.R.K – Brackenvale Auto Detailing – Business Card</title>
<link rel="stylesheet" href="https://fonts.googleapis.com/css2?family=Exo+2:ital,wght@0,900;1,800;1,900&display=swap">
<style>
  :root {
    --silver-light: #f2f3f5;
    --silver-mid: #b9bec6;
    --silver-dark: #6c737c;
    --stripe-navy: #1e2f8c;
    --stripe-teal: #5fb3bd;
    --brand-pink: #ee2a7b;
    --panel-pink-dark: #9e2a45;
    --panel-pink-light: #d9607a;
    --panel-edge: #f4f4f4;
    --label-red: #ff2a55;
    --text-white: #ffffff;
    --wheel-pink: #e0467f;
    --wheel-deep: #5a1830;
    --wheel-chrome: #cfd3d8;
  }

  html, body {
    margin: 0;
    padding: 0;
    width: 1200px;
    height: 685px;
    overflow: hidden;
    background: #ffffff;
  }

  .business-card {
    position: relative;
    width: 1200px;
    height: 685px;
    overflow: hidden;
    font-family: "Exo 2", sans-serif;
    background:
      repeating-linear-gradient(150deg,
        transparent 0 70px,
        var(--stripe-navy) 70px 84px,
        transparent 84px 150px,
        var(--stripe-teal) 150px 158px,
        transparent 158px 200px),
      radial-gradient(ellipse at 45% 45%, var(--silver-light) 0%, var(--silver-mid) 55%, var(--silver-dark) 100%);
  }

  .wheel-feature {
    position: absolute;
    left: 573px;
    top: 267px;
    width: 760px;
    height: 760px;
    border-radius: 50%;
    background: radial-gradient(circle at 40% 40%, var(--wheel-pink) 0%, #c23a6c 40%, var(--wheel-deep) 75%, #2a0c18 100%);
    opacity: 0.92;
  }

  .brand-name {
    position: absolute;
    left: 133px;
    top: 20px;
    width: 1014px;
    margin: 0;
    font-weight: 900;
    font-style: normal;
    font-size: 300px;
    line-height: 1;
    letter-spacing: 6px;
    text-align: center;
    color: var(--brand-pink);
  }

  .contact-panel {
    position: absolute;
    left: 60px;
    top: 387px;
    width: 560px;
    height: 233px;
    border-radius: 40px;
    border: 3px solid var(--panel-edge);
    box-sizing: border-box;
    background: linear-gradient(90deg, var(--panel-pink-dark) 0%, var(--panel-pink-light) 100%);
    overflow: hidden;
  }

  .panel-wheel {
    position: absolute;
    right: -10px;
    top: 0;
    width: 228px;
    height: 228px;
    border-radius: 50%;
    background: radial-gradient(circle, #eef0f2 0%, var(--wheel-chrome) 45%, #4a4e55 80%, #1b1d21 100%);
  }

  .contact-details {
    position: absolute;
    left: 22px;
    top: 50px;
    margin: 0;
    font-style: italic;
    font-weight: 800;
    color: var(--text-white);
  }

  .address-line {
    display: block;
    font-size: 22px;
    line-height: 25px;
    text-transform: uppercase;
    letter-spacing: 0.5px;
  }

  .phone-row {
    display: block;
    white-space: nowrap;
    line-height: 48px;
  }

  .phone-row:first-of-type { margin-top: 8px; }

  .phone-label {
    font-size: 26px;
    color: var(--label-red);
    font-weight: 900;
    margin-right: 10px;
  }

  .phone-number {
    font-size: 50px;
    font-weight: 900;
    letter-spacing: 1px;
  }
</style>
</head>
<body>
  <main class="business-card">
    <div class="wheel-feature" role="img" aria-label="Close-up of a pink alloy car wheel"></div>

    <h1 class="brand-name">B.R.K</h1>

    <section class="contact-panel" aria-label="Brackenvale Auto Detailing contact details">
      <div class="panel-wheel" role="img" aria-label="Chrome alloy wheel"></div>
      <address class="contact-details">
        <span class="address-line">42 Tillbury Crs</span>
        <span class="address-line">Brackenvale Vic 3819</span>
        <span class="phone-row"><span class="phone-label">PH:</span><span class="phone-number">(03)58264027</span></span>
        <span class="phone-row"><span class="phone-label">MOB:</span><span class="phone-number">(04)17392658</span></span>
      </address>
    </section>
  </main>
</body>
</html>
```